The Timber Loft

We need a business card design for our wardrobe company.
Please visit our website www.zorvelcabinets.com to get an idea of who we are.

```html
<!DOCTYPE html>
<html lang="en">
<head>
<meta charset="utf-8">
<title>The Timber Loft – Business Card</title>
<link rel="stylesheet" href="https://fonts.googleapis.com/css2?family=Montserrat:wght@400;500;600&display=swap">
<style>
  :root {
    --backdrop: #d9dadc;
    --card: #2b2a29;
    --gold: #9a8359;
    --white: #f4f2ee;
    --emboss: #1c1b1a;
    --emboss-light: #3a3938;
  }
  * { margin: 0; padding: 0; box-sizing: border-box; }
  html, body { width: 1200px; height: 800px; overflow: hidden; }
  body {
    background: var(--backdrop);
    font-family: "Montserrat", sans-serif;
    position: relative;
  }
  .card {
    position: absolute;
    width: 540px;
    height: 308px;
    background: var(--card);
    border-radius: 3px;
    box-shadow: 0 6px 18px rgba(0,0,0,0.25);
  }
  /* Reverse side */
  .card--back { left: 600px; top: 70px; }
  .back-brand {
    position: absolute;
    left: 0; right: 0; top: 112px;
    display: flex; align-items: center; justify-content: center; gap: 16px;
  }
  .back-brand .mark {
    width: 44px; height: 44px;
    background: var(--emboss);
    box-shadow: inset 1px 1px 0 var(--emboss-light);
  }
  .back-brand .words { color: var(--emboss); }
  .back-brand .name {
    font-size: 17px; font-weight: 500; letter-spacing: 2px; text-transform: uppercase;
    text-shadow: 0 1px 0 var(--emboss-light);
  }
  .back-brand .tagline {
    font-size: 14px; font-weight: 500; margin-top: 4px;
    text-shadow: 0 1px 0 var(--emboss-light);
  }
  /* Front side */
  .card--front { left: 110px; top: 410px; }
  .front-brand {
    position: absolute; left: 34px; top: 94px; width: 230px; text-align: center;
  }
  .front-brand .mark {
    width: 38px; height: 38px; background: var(--gold); margin: 0 auto 14px;
  }
  .front-brand .name {
    color: var(--white); font-size: 17px; font-weight: 500;
    letter-spacing: 2px; text-transform: uppercase;
  }
  .front-brand .tagline {
    color: var(--white); font-size: 13px; font-weight: 400; margin-top: 4px;
  }
  .divider {
    position: absolute; left: 288px; top: 76px; width: 1px; height: 128px;
    background: var(--gold);
  }
  .contact { position: absolute; left: 306px; top: 84px; color: var(--white); }
  .contact .person { color: var(--gold); font-size: 16px; font-weight: 600; }
  .contact .role { font-size: 12px; margin: 3px 0 14px; }
  .contact ul { list-style: none; }
  .contact li {
    display: flex; align-items: center; gap: 8px;
    font-size: 12px; line-height: 19px;
  }
  .contact svg { width: 11px; height: 11px; flex: none; }
  .address {
    position: absolute; left: 0; right: 0; bottom: 40px;
    text-align: center; color: var(--white); font-size: 13px;
  }
</style>
</head>
<body>

  <section class="card card--back" aria-label="Card reverse">
    <div class="back-brand">
      <span class="mark"></span>
      <div class="words">
        <div class="name">The Timber Loft</div>
        <div class="tagline">Made to Fit Every Room</div>
      </div>
    </div>
  </section>

  <section class="card card--front" aria-label="Card front">
    <div class="front-brand">
      <div class="mark"></div>
      <div class="name">The Timber Loft</div>
      <div class="tagline">Made to Fit Every Room</div>
    </div>

    <div class="divider"></div>

    <div class="contact">
      <div class="person">Mira Valden</div>
      <div class="role">Interior Planner &amp; Space Advisor</div>
      <ul>
        <li>
          <svg viewBox="0 0 12 12"><path d="M2.5 1 L4.5 1 L5.2 3.4 L3.9 4.4 Q5 7 7.6 8.1 L8.6 6.8 L11 7.5 L11 9.5 Q10.5 11 9 11 Q1 10 1 3 Q1 1.5 2.5 1 Z" fill="var(--gold)"/></svg>
          0207 555 0184
        </li>
        <li>
          <svg viewBox="0 0 12 12"><rect x="0.7" y="2.2" width="10.6" height="7.6" fill="none" stroke="var(--gold)" stroke-width="1.1"/><path d="M0.9 2.5 L6 6.6 L11.1 2.5" fill="none" stroke="var(--gold)" stroke-width="1.1"/></svg>
          mira@zorvelcabinets.com
        </li>
        <li>
          <svg viewBox="0 0 12 12" fill="none" stroke="var(--gold)" stroke-width="1"><circle cx="6" cy="6" r="5"/><ellipse cx="6" cy="6" rx="2.2" ry="5"/><path d="M1 6 H11 M1.8 3.4 H10.2 M1.8 8.6 H10.2"/></svg>
          www.zorvelcabinets.com
        </li>
      </ul>
    </div>

    <div class="address">Alder Court, 42 Hollow Lane, London N4 7QT</div>
  </section>

</body>
</html>
```